Honey Label for 1kg square jar

We require premium looking honey label for 1kg packed in dark amber jar as shown in the image.
Brand is called :"Velmora Honey" - logo to be provided
We would like the following colours to be considered (white, gold and red)
We like to have some flowers and beehives on the background.
The label covers 3 sides of the square jar and were hoping to see render of the front side which should include the brand and also the words" 100% Premium Australian Honey"

Need extra days to review

```html
<!DOCTYPE html>
<html lang="en">
<head>
<meta charset="utf-8">
<title>Velmora Honey – 1kg Jar Label</title>
<link rel="stylesheet" href="https://fonts.googleapis.com/css2?family=Cinzel:wght@500&family=Montserrat:wght@600;700&display=swap">
<style>
  :root {
    --backdrop: #f2dcb2;
    --label-gold: #c98a1c;
    --label-white: #ffffff;
    --label-yellow: #fcd77a;
    --label-yellow-light: #ffe7a6;
    --ink-brown: #3a210f;
    --mark-tone: #e8a72a;
    --banner-gold: #c8861a;
  }
  * { margin: 0; padding: 0; box-sizing: border-box; }
  html, body {
    width: 1200px;
    height: 1200px;
    overflow: hidden;
    background: var(--backdrop);
  }
  .canvas {
    position: relative;
    width: 1200px;
    height: 1200px;
    display: flex;
    align-items: center;
    justify-content: center;
  }
  .label {
    width: 700px;
    height: 830px;
    border-radius: 90px;
    background: var(--label-gold);
    padding: 14px;
  }
  .label-ring {
    width: 100%;
    height: 100%;
    border-radius: 78px;
    background: var(--label-white);
    padding: 14px;
  }
  .label-face {
    position: relative;
    width: 100%;
    height: 100%;
    border-radius: 66px;
    overflow: hidden;
  }
  .label-background {
    position: absolute;
    inset: 0;
    background: radial-gradient(ellipse at 50% 35%, var(--label-yellow-light) 0%, var(--label-yellow) 75%);
  }
  .label-content {
    position: relative;
    height: 100%;
    display: flex;
    flex-direction: column;
    align-items: center;
    padding-top: 62px;
  }
  .brand-mark {
    width: 300px;
    height: 300px;
    border-radius: 50%;
    background: var(--mark-tone);
  }
  .brand-name {
    margin-top: 48px;
    font-family: "Cinzel", serif;
    font-weight: 500;
    color: var(--ink-brown);
    text-align: center;
    line-height: 1;
  }
  .brand-name .word-main {
    display: block;
    font-size: 104px;
    letter-spacing: 2px;
  }
  .brand-name .word-sub {
    display: block;
    margin-top: 10px;
    font-size: 46px;
    letter-spacing: 30px;
    padding-left: 30px;
  }
  .claim-banner {
    margin-top: 26px;
    background: var(--banner-gold);
    color: var(--label-white);
    font-family: "Montserrat", sans-serif;
    font-weight: 700;
    font-size: 24px;
    letter-spacing: 0.5px;
    padding: 6px 18px;
  }
  .net-weight {
    margin-top: 34px;
    font-family: "Montserrat", sans-serif;
    font-weight: 700;
    font-size: 24px;
    color: var(--ink-brown);
  }
</style>
</head>
<body>
  <main class="canvas">
    <section class="label">
      <div class="label-ring">
        <div class="label-face">
          <div class="label-background" role="img" aria-label="Soft golden background with a faint honeycomb pattern"></div>
          <div class="label-content">
            <div class="brand-mark" aria-hidden="true"></div>
            <h1 class="brand-name">
              <span class="word-main">VELMORA</span>
              <span class="word-sub">HONEY</span>
            </h1>
            <p class="claim-banner">100% PREMIUM AUSTRALIAN HONEY</p>
            <p class="net-weight">NETTO: 1 Kg</p>
          </div>
        </div>
      </div>
    </section>
  </main>
</body>
</html>
```